Cyber Security Site Design (Products & Consulting)

I need my website redesigned to be engaging, clean, efficient and modern. My company (when its up and running) is going to be concentrated on two things: a few specific products for cyber security as well as cyber security consulting services. The background I bring to the field is having worked with small companies all the way to the largest government organizations and advising them on their security posture and how to improve it. We need the ability to add products and services easily.

For a sample product, you can use either Tarnel (http://www.tarnel-relay.org/) or Vornidex Graywell (https://www.vornidex.com/products/relay-kx-and-enhanced-safe-portal).

It will replace https://dalmorenvue.com/

Target Market(s)

Cyber Security professionals in all verticals

Coding

Coded - Design and coding required

Number of Pages Required

4 page

Font styles to use
Sans Serif

Colors
6b449b

Requirements
Must have
• Ability to easily modify
• Have main page
• Have product specific pages
• Have consulting services pages
• Have executive team information
• Clean, modern design
• Usage of the logo and its color scheme
Nice to have
• I like the idea of a left collapsed sidebar (so icons only) that can expand for text.
• I am also open to a very unique landing page, possibly a shape in the middle (hexagons maybe?) with each of the options there.
Should not have
• Nothing that looks like it came out of a hacker movie

```html
<!DOCTYPE html>
<html lang="en">
<head>
<meta charset="utf-8">
<title>Dalmoren Vue – Cyber Security Products & Consulting</title>
<link rel="stylesheet" href="https://fonts.googleapis.com/css2?family=Mulish:wght@400;600;700;800&family=Saira+Condensed:wght@600;700&family=Montserrat:wght@600;700&display=swap">
<style>
:root{
  --purple:#6b449b;
  --purple-dark:#4e2f78;
  --purple-soft:#8a66b8;
  --ink:#222;
  --text:#555;
  --muted:#888;
  --line:#e6e6ea;
  --grey-bg:#f4f4f6;
  --white:#fff;
  --dark:#1d2230;
}
*{box-sizing:border-box;margin:0;padding:0}
html,body{width:1200px;height:4500px;overflow:hidden}
body{font-family:"Mulish",sans-serif;color:var(--text);background:var(--white);font-size:14px}
.section-title{font-family:"Saira Condensed",sans-serif;font-weight:700;font-size:34px;letter-spacing:1px;color:var(--ink);text-align:center;text-transform:uppercase}
.title-mark{display:block;width:16px;height:16px;margin:10px auto 0;border:3px solid var(--purple);border-radius:3px}

/* header */
.site-header{height:114px;position:relative;border-bottom:1px solid var(--line)}
.brand{position:absolute;left:105px;top:18px;display:flex;align-items:center;gap:12px}
.brand-dot{width:56px;height:56px;border-radius:50%;background:var(--purple)}
.brand-name{font-family:"Mulish",sans-serif;font-weight:800;font-size:34px;color:var(--purple);letter-spacing:1px}
.contact-bar{position:absolute;right:105px;top:16px;display:flex;align-items:center;gap:18px;font-size:14px;color:var(--ink)}
.contact-item{display:flex;align-items:center;gap:8px}
.contact-icon{width:24px;height:24px;border-radius:50%;background:var(--purple);display:flex;align-items:center;justify-content:center}
.social{display:flex;gap:6px}
.social span{width:22px;height:22px;border-radius:50%;background:var(--purple)}
.main-nav{position:absolute;right:105px;top:74px;display:flex;gap:40px;font-size:14px;font-weight:700;color:var(--ink)}
.main-nav a{color:inherit;text-decoration:none;padding-bottom:8px}
.main-nav a.active{color:var(--purple);border-bottom:3px solid var(--purple)}

/* hero */
.hero{height:549px;position:relative;background:linear-gradient(180deg,#1b2d57 0%,#2f4f86 35%,#4d5e7a 60%,#20232f 100%)}
.hero-arrow{position:absolute;top:245px;width:34px;height:34px;border-radius:50%;border:2px solid rgba(255,255,255,.8);display:flex;align-items:center;justify-content:center}
.hero-arrow.left{left:48px}.hero-arrow.right{right:48px}
.hero-headline{position:absolute;left:0;right:0;top:438px;text-align:center;font-family:"Montserrat",sans-serif;font-weight:700;font-size:32px;line-height:1.4;color:var(--white);letter-spacing:1px;text-transform:uppercase}

/* about */
.about{height:327px;padding-top:70px}
.about p{width:900px;margin:0 auto;text-align:center;font-size:15px;line-height:1.9}
.about-body{margin-top:28px}

/* services */
.services{height:705px;background:var(--grey-bg);padding-top:70px}
.service-grid{position:relative;width:900px;margin:58px auto 0;display:grid;grid-template-columns:repeat(3,300px);grid-template-rows:225px 225px}
.service{padding:20px 40px;text-align:center}
.service:nth-child(-n+3){border-bottom:1px solid #d8d8de}
.service:nth-child(2),.service:nth-child(5){border-left:1px solid #d8d8de;border-right:1px solid #d8d8de}
.service.featured{background:var(--purple);color:var(--white);margin:-10px 0 16px;border-radius:4px;box-shadow:0 10px 24px rgba(107,68,155,.35)}
.service h3{font-family:"Saira Condensed",sans-serif;font-weight:600;font-size:18px;color:var(--ink);letter-spacing:.5px;margin:12px 0 8px;text-transform:uppercase}
.service.featured h3{color:var(--white)}
.service p{font-size:13px;line-height:1.55}
.service svg{display:block;margin:10px auto 0}
.grid-dot{position:absolute;top:220px;width:10px;height:10px;border-radius:50%;background:var(--purple)}

/* products */
.products{height:515px;padding-top:82px}
.product-row{display:flex;justify-content:center;gap:36px;margin-top:50px}
.product-card{width:462px;height:240px;background:var(--white);box-shadow:0 4px 18px rgba(0,0,0,.09);border-radius:4px;display:flex;padding:30px 24px;gap:26px}
.product-box{flex:0 0 150px;width:150px;height:180px;border-radius:3px}
.product-box.teal{background:linear-gradient(135deg,#e9eef0,#32b3b0 60%,#1d8e94)}
.product-box.amber{background:linear-gradient(135deg,#eeeeee,#f3c514 60%,#d9a400)}
.product-info{flex:1}
.product-info h3{font-family:"Saira Condensed",sans-serif;font-weight:700;font-size:26px;color:var(--purple);letter-spacing:1px}
.product-info p{font-size:13px;line-height:1.6;margin-top:10px}
.product-info a{display:inline-block;margin-top:12px;font-size:13px;color:var(--purple);text-decoration:none}

/* more security */
.more-security{height:420px;background:var(--grey-bg);position:relative}
.security-photo{position:absolute;left:150px;top:60px;width:290px;height:290px;border-radius:50%;background:radial-gradient(circle at 40% 40%,#dcd6cc,#8c8f96 70%,#3b3f4c)}
.security-copy{position:absolute;left:490px;top:90px;width:580px}
.security-copy h2{font-family:"Saira Condensed",sans-serif;font-weight:700;font-size:32px;color:var(--ink);text-transform:uppercase}
.security-copy h4{font-size:17px;font-weight:800;color:var(--ink);margin:8px 0 16px}
.security-copy p{font-size:13px;line-height:1.7}
.cta{display:inline-flex;align-items:center;margin-top:22px}
.cta-mark{width:40px;height:40px;border-radius:50%;border:4px solid var(--ink);background:var(--white)}
.cta-label{background:var(--purple);color:var(--white);font-weight:700;font-size:15px;letter-spacing:1px;padding:10px 28px 10px 18px;text-transform:uppercase;margin-left:-4px}

/* team */
.team{height:545px;padding-top:120px}
.team-row{display:flex;justify-content:center;gap:12px;margin-top:48px}
.member{width:222px;height:220px;background:var(--white);border:1px solid var(--line);box-shadow:0 2px 10px rgba(0,0,0,.05);text-align:center;padding-top:30px}
.member-photo{width:110px;height:110px;border-radius:50%;margin:0 auto;background:radial-gradient(circle at 50% 40%,#d9c4b3,#8b7566 70%,#5a4a42)}
.member h3{font-size:15px;font-weight:800;color:var(--ink);margin-top:18px}
.member p{font-size:12px;color:var(--muted);margin-top:4px;text-transform:uppercase}
.pager{display:flex;justify-content:center;gap:10px;margin-top:32px}
.pager span{width:26px;height:26px;border-radius:50%;border:1px solid #ccc}
.pager span.on{border-color:var(--ink)}

/* stats */
.stats{height:240px;background:linear-gradient(90deg,var(--purple-dark),var(--purple) 50%,var(--purple-dark));display:flex;justify-content:center;color:var(--white)}
.stat{width:225px;text-align:center;padding-top:44px}
.stat-value{font-family:"Montserrat",sans-serif;font-weight:600;font-size:48px;line-height:1.1;margin-top:10px}
.stat-label{font-size:15px;font-weight:700;text-transform:uppercase;letter-spacing:.5px}

/* reviews */
.reviews{height:495px;padding-top:80px;position:relative}
.review-row{position:relative;height:240px;margin-top:52px}
.review{position:absolute;text-align:center;padding:26px 30px;width:380px}
.review.side{top:40px;opacity:.45;width:330px;font-size:11px}
.review.side.l{left:130px}.review.side.r{right:130px}
.review.main{left:410px;width:380px;background:var(--white);box-shadow:0 6px 24px rgba(0,0,0,.12);height:228px;z-index:1}
.quote{font-family:"Montserrat",sans-serif;font-size:34px;color:var(--purple);line-height:.7}
.review h3{font-size:16px;font-weight:800;color:var(--purple);margin:8px 0}
.review p{font-size:12px;line-height:1.6}
.review .author{margin-top:12px;font-size:12px;font-weight:800;color:var(--ink)}
.review .company{font-size:11px;color:var(--muted)}
.review-arrow{position:absolute;top:100px;color:var(--muted);font-size:18px}

/* location */
.location{height:530px;position:relative;background:linear-gradient(135deg,#2b3348,#1a1f2d 55%,#232838)}
.location h2{position:absolute;left:228px;top:70px;font-family:"Saira Condensed",sans-serif;font-weight:700;font-size:34px;color:var(--white);text-transform:uppercase}
.location .loc-text{position:absolute;left:228px;top:122px;width:330px;font-size:14px;line-height:1.6;color:#dfe0e6}
.map{position:absolute;left:228px;top:190px;width:435px;height:270px;background:linear-gradient(135deg,#e8e6e1,#d6dbe0)}
.help-form{position:absolute;left:665px;top:140px;width:310px;height:390px;background:var(--white);border:3px solid var(--purple);padding:22px 28px}
.help-form h2{position:static;font-family:"Saira Condensed",sans-serif;font-size:32px;color:var(--purple)}
.help-form .sub{font-size:11px;color:var(--muted)}
.field{border-bottom:1px solid #ccc;font-size:11px;color:var(--muted);padding:16px 0 6px}
.field.tall{height:70px}
.submit{display:inline-flex;align-items:center;margin-top:22px}
.submit .cta-mark{width:34px;height:34px;border-width:3px}
.submit .cta-label{font-size:13px;padding:8px 16px}

/* footer */
.site-footer{height:60px;background:var(--purple);color:var(--white);display:flex;align-items:center;justify-content:space-between;padding:0 150px;font-size:13px}
.site-footer .social span{background:var(--white);opacity:.9}
</style>
</head>
<body>

<header class="site-header">
  <div class="brand"><span class="brand-dot"></span><span class="brand-name">DALMOREN VUE</span></div>
  <div class="contact-bar">
    <span class="contact-item"><span class="contact-icon"><svg width="12" height="12" viewBox="0 0 24 24"><path fill="#fff" d="M6.6 10.8a15 15 0 006.6 6.6l2.2-2.2c.3-.3.7-.4 1-.2 1.1.4 2.3.6 3.6.6.6 0 1 .4 1 1V20c0 .6-.4 1-1 1A17 17 0 013 4c0-.6.4-1 1-1h3.5c.6 0 1 .4 1 1 0 1.3.2 2.5.6 3.6.1.3 0 .7-.2 1z"/></svg></span>(012) 555 0147</span>
    <span class="contact-item"><span class="contact-icon"><svg width="12" height="12" viewBox="0 0 24 24"><path fill="#fff" d="M2 5h20v14H2zm2 2v.5l8 5 8-5V7l-8 5z"/></svg></span>inquiry@dalmorenvue.com</span>
    <span class="social"><span></span><span></span><span></span><span></span></span>
  </div>
  <nav class="main-nav">
    <a class="active" href="#">HOME</a><a href="#">SERVICES</a><a href="#">OUR TEAM</a><a href="#">PRODUCTS</a><a href="#">CONTACT US</a>
  </nav>
</header>

<section class="hero" role="img" aria-label="Night skyline of a downtown city with lit office towers">
  <span class="hero-arrow left"><svg width="12" height="12" viewBox="0 0 12 12"><path d="M8 1L3 6l5 5" stroke="#fff" stroke-width="2" fill="none"/></svg></span>
  <span class="hero-arrow right"><svg width="12" height="12" viewBox="0 0 12 12"><path d="M4 1l5 5-5 5" stroke="#fff" stroke-width="2" fill="none"/></svg></span>
  <h1 class="hero-headline">We provide early detection, immediate<br>remediation and proactive preventive measures</h1>
</section>

<section class="about">
  <h2 class="section-title">About Us</h2><span class="title-mark"></span>
  <div class="about-body">
    <p>We are a company that takes its roots from the idea of providing appropriate and creative solutions for cyber security operations, development and management. We have a mission first mindset for our clients and their objectives.</p>
    <p style="margin-top:10px">We are located in the Corvale / Linwick area but are able to work with clients world-wide. Please contact us for any inquires you may have and we will be glad to assist you in any way possible.</p>
  </div>
</section>

<section class="services">
  <h2 class="section-title">Cyber Security Consulting Services</h2><span class="title-mark"></span>
  <div class="service-grid">
    <div class="service">
      <svg width="56" height="56" viewBox="0 0 56 56" fill="none" stroke="#6b449b" stroke-width="2"><circle cx="28" cy="18" r="9"/><path d="M10 50c2-12 9-17 18-17s16 5 18 17"/><path d="M24 33l4 8 4-8"/></svg>
      <h3>Virtual CISO / vISO</h3>
      <p>Adipiscing elit sed autem eiusmodte mporal laboratories dolore magna aliqua renim adim minim veniam quis.</p>
    </div>
    <div class="service featured">
      <svg width="56" height="56" viewBox="0 0 56 56" fill="none" stroke="#fff" stroke-width="2"><rect x="18" y="18" width="20" height="20" rx="2"/><path d="M23 18v-8M28 18v-8M33 18v-8M23 38v8M28 38v8M33 38v8M18 23h-8M18 28h-8M18 33h-8M38 23h8M38 28h8M38 33h8"/></svg>
      <h3>Cyber Security</h3>
      <p>Adipiscing elit sed autem eiusmodte mporal laboratories dolore magna aliqua renim adim minim veniam quis.</p>
    </div>
    <div class="service">
      <svg width="56" height="56" viewBox="0 0 56 56" fill="none" stroke="#6b449b" stroke-width="2"><circle cx="24" cy="24" r="14"/><path d="M34 34l14 14"/><path d="M24 16v10M24 30v2"/></svg>
      <h3>Incident Response</h3>
      <p>Adipiscing elit sed autem eiusmodte mporal laboratories dolore magna aliqua renim adim minim veniam quis.</p>
    </div>
    <div class="service">
      <svg width="56" height="56" viewBox="0 0 56 56" fill="none" stroke="#6b449b" stroke-width="2"><circle cx="28" cy="16" r="6"/><circle cx="12" cy="30" r="5"/><circle cx="44" cy="30" r="5"/><path d="M18 44c1-7 5-10 10-10s9 3 10 10M4 46c1-5 4-7 8-7M52 46c-1-5-4-7-8-7"/></svg>
      <h3>Risk Assessment</h3>
      <p>Adipiscing elit sed autem eiusmodte mporal laboratories dolore magna aliqua renim adim minim veniam quis.</p>
    </div>
    <div class="service">
      <svg width="56" height="56" viewBox="0 0 56 56" fill="none" stroke="#6b449b" stroke-width="2"><path d="M28 6l18 7v13c0 12-8 21-18 24-10-3-18-12-18-24V13z"/><rect x="21" y="26" width="14" height="11" rx="1"/><path d="M24 26v-4a4 4 0 018 0v4"/></svg>
      <h3>Network Security</h3>
      <p>Adipiscing elit sed autem eiusmodte mporal laboratories dolore magna aliqua renim adim minim veniam quis.</p>
    </div>
    <div class="service">
      <svg width="56" height="56" viewBox="0 0 56 56" fill="none" stroke="#6b449b" stroke-width="2"><rect x="6" y="10" width="44" height="28" rx="2"/><path d="M20 46h16M28 38v8"/><path d="M20 24l6 6 10-11"/></svg>
      <h3>Managed Security Services</h3>
      <p>Adipiscing elit sed autem eiusmodte mporal laboratories dolore magna aliqua renim adim minim veniam quis.</p>
    </div>
    <span class="grid-dot" style="left:295px"></span>
    <span class="grid-dot" style="left:595px"></span>
  </div>
</section>

<section class="products">
  <h2 class="section-title">Products</h2><span class="title-mark"></span>
  <div class="product-row">
    <article class="product-card">
      <div class="product-box teal" role="img" aria-label="Tarnel cyber security product box"></div>
      <div class="product-info">
        <h3>PRODUCT 1</h3>
        <p>Morbi convallis bibendum urna ut viverra. Maecenas quis consequat libero, a feugiat eros. Nunc ut lacinia tortor morbi ultricies laoreet ullamcorper phasellus semper.</p>
        <a href="#">View Details →</a>
      </div>
    </article>
    <article class="product-card">
      <div class="product-box amber" role="img" aria-label="Vornidex Graywell cyber security product box"></div>
      <div class="product-info">
        <h3>PRODUCT 2</h3>
        <p>Morbi convallis bibendum urna ut viverra. Maecenas quis consequat libero, a feugiat eros. Nunc ut lacinia tortor morbi ultricies laoreet ullamcorper phasellus semper.</p>
        <a href="#">View Details →</a>
      </div>
    </article>
  </div>
</section>

<section class="more-security">
  <div class="security-photo" role="img" aria-label="Team working together at an office table with laptops"></div>
  <div class="security-copy">
    <h2>You Need More Security?</h2>
    <h4>Aliquam sapien est, mollis id mattis id, scelerisque sed dolor.</h4>
    <p>Proin accumsan erat sem, id porta risus dignissim ac. Vestibulum nec sapien in lacus ornare nec nec justo. Aliquam sapien est, mollis id mattis id, scelerisque sed dolor. Proin accumsan erat sem, id porta risus dignissim ac. Vestibulum nec sapien in lacus ornare nec nec justo.</p>
    <a class="cta"><span class="cta-mark"></span><span class="cta-label">Contact Us Today</span></a>
  </div>
</section>

<section class="team">
  <h2 class="section-title">Our Team</h2><span class="title-mark"></span>
  <div class="team-row">
    <div class="member"><div class="member-photo" role="img" aria-label="Portrait of Marten Kolby Ashgrove"></div><h3>Marten Kolby Ashgrove</h3><p style="text-transform:none">Founder &amp; CEO</p></div>
    <div class="member"><div class="member-photo" role="img" aria-label="Portrait of Delia Varrow"></div><h3>Delia Varrow</h3><p>Associate</p></div>
    <div class="member"><div class="member-photo" role="img" aria-label="Portrait of Rufino Castelle"></div><h3>Rufino Castelle</h3><p>Nisllacus</p></div>
    <div class="member"><div class="member-photo" role="img" aria-label="Portrait of Nessa Orlin"></div><h3>Nessa Orlin</h3><p>Nisllacus</p></div>
  </div>
  <div class="pager"><span></span><span class="on"></span></div>
</section>

<section class="stats">
  <div class="stat">
    <svg width="60" height="44" viewBox="0 0 60 44" fill="none" stroke="#f3a46b" stroke-width="2"><circle cx="30" cy="12" r="7"/><circle cx="12" cy="16" r="5"/><circle cx="48" cy="16" r="5"/><path d="M18 42c0-9 5-14 12-14s12 5 12 14M2 40c0-6 4-10 10-10M58 40c0-6-4-10-10-10"/></svg>
    <div class="stat-value">120</div><div class="stat-label">About Employee</div>
  </div>
  <div class="stat">
    <svg width="50" height="44" viewBox="0 0 50 44" fill="none" stroke="#f3a46b" stroke-width="2"><path d="M4 42h42"/><rect x="8" y="24" width="7" height="18"/><rect x="21" y="14" width="7" height="28"/><rect x="34" y="4" width="7" height="38"/></svg>
    <div class="stat-value">250</div><div class="stat-label">Queries Solved</div>
  </div>
  <div class="stat">
    <svg width="44" height="44" viewBox="0 0 44 44" fill="none" stroke="#f3a46b" stroke-width="2"><circle cx="22" cy="22" r="20"/><circle cx="22" cy="17" r="7"/><path d="M9 36c3-6 7-9 13-9s10 3 13 9"/></svg>
    <div class="stat-value">550</div><div class="stat-label">Registered Users</div>
  </div>
  <div class="stat">
    <svg width="44" height="44" viewBox="0 0 44 44" fill="none" stroke="#f3a46b" stroke-width="2"><circle cx="22" cy="22" r="20"/><circle cx="15" cy="17" r="1.5" fill="#f3a46b"/><circle cx="29" cy="17" r="1.5" fill="#f3a46b"/><path d="M13 26c4 6 14 6 18 0"/></svg>
    <div class="stat-value">1000</div><div class="stat-label">Happy Customers</div>
  </div>
</section>

<section class="reviews">
  <h2 class="section-title">Customer Reviews</h2><span class="title-mark"></span>
  <div class="review-row">
    <div class="review side l"><div class="quote">“</div><h3 style="font-size:13px">Lorem Ipsum Dolor Sit Am...</h3><p>Ut enim ad minim veniam dolor aliqua magna tempor nisi aliquip commodo duis aute irure in voluptate velit esse.</p><div class="author">Client Name, Company</div></div>
    <span class="review-arrow" style="left:400px">‹</span>
    <div class="review main"><div class="quote">“</div><h3>Lorem Ipsum Dolor Sit Amet ...</h3><p>Ut enim ad minim veniam dolor aliqua magna tempor adipiscing. Expedita animo molestie aliquam hic ab dolorem qui fuega voluptates pariatur aut mi rapellat. Quo quer voluptas incidunt tenetur consectetur sunt laudantium vel at.</p><div class="author">Nadia Wren, Pharetrum</div><div class="company">QUODIG VULPUTAT</div></div>
    <span class="review-arrow" style="left:790px">›</span>
    <div class="review side r"><div class="quote">“</div><h3 style="font-size:13px">Lorem Ipsum Dolor Sit Am...</h3><p>Sed ut perspiciatis unde omnis iste natus error sit voluptatem accusantium doloremque laudantium totam rem aperiam.</p><div class="author">Client Name, Company</div></div>
  </div>
</section>

<section class="location" aria-label="Our location">
  <h2>Our Location</h2>
  <p class="loc-text">Aliquam sapien est, mollis id mattis id, scelerisque sed dolor proin accumsan erat sem.</p>
  <div class="map" role="img" aria-label="Street map with corporate office marker"></div>
  <form class="help-form">
    <h2>Need Help?</h2>
    <p class="sub">Fill out the form below to get connected</p>
    <div class="field">Name *</div>
    <div class="field">Email *</div>
    <div class="field">Subject *</div>
    <div class="field tall">Message *</div>
    <span class="submit"><span class="cta-mark"></span><span class="cta-label">Submit</span></span>
  </form>
</section>

<footer class="site-footer">
  <span>COPYRIGHT © 2018 DALMOREN VUE. ALL RIGHTS RESERVED.</span>
  <span class="social"><span></span><span></span><span></span><span></span></span>
</footer>

</body>
</html>
```